Business Card Design for Concierge business

Hi. I would like to have an elegant, smart business card for my concierge business, called Harbor Concierge. The services I provide are mail management, dog walking, cleaning, car, stylist, personal shopper, running errands, property management, event planning. I was thinking to add my picture but I would like to see options without it as well, if possible.

Thank you.

Business Card Details:
*Designers are to solely use contact information for the business card design. This is not to be used to contact the customer*

Name: Tamsin Heller
mail: quaylineerrands@mailvora.net
Phone: 305-482-9167

Target Market(s)

vacation home owners

Industry/Entity Type

Business

Font styles to use
Serif

Colors

Designer to choose colors to be used in the design.

Requirements
Nice to have
• Could use icons that describe the services I provide for example car, house, key, shopping cart, shopping bags, envelope, champagne glasses, phone, dog etc.

```html
<!DOCTYPE html>
<html lang="en">
<head>
<meta charset="utf-8">
<title>Harbor Concierge – Business Card</title>
<link rel="stylesheet" href="https://fonts.googleapis.com/css2?family=Cormorant+Garamond:wght@500&family=Montserrat:wght@500&display=swap">
<style>
  :root {
    --backdrop: #e9e7e3;
    --card-black: #141414;
    --card-sheen: #262626;
    --gold: #c9a43e;
    --ivory: #f4f2ee;
    --photo-dark: #2a1f1c;
    --photo-mid: #6b4a3f;
    --photo-light: #b88e7c;
  }
  * { box-sizing: border-box; margin: 0; padding: 0; }
  html, body { width: 1200px; height: 1000px; overflow: hidden; }
  body {
    background: var(--backdrop);
    display: flex;
    flex-direction: column;
    align-items: center;
    justify-content: center;
    gap: 60px;
  }
  .card {
    position: relative;
    width: 700px;
    height: 400px;
    background: radial-gradient(ellipse at 40% 30%, var(--card-sheen), var(--card-black) 70%);
    box-shadow: 0 10px 30px rgba(0,0,0,.25);
    overflow: hidden;
  }

  /* Front: business name and email */
  .card-front {
    display: flex;
    flex-direction: column;
    align-items: center;
    justify-content: center;
    gap: 40px;
  }
  .business-name {
    font-family: "Cormorant Garamond", serif;
    font-weight: 500;
    color: var(--ivory);
    font-size: 54px;
    line-height: 1;
  }
  .email {
    font-family: "Montserrat", sans-serif;
    font-weight: 500;
    font-size: 15px;
    color: var(--gold);
    letter-spacing: .3px;
  }

  /* Back: title, portrait area, contact */
  .card-back .title {
    position: absolute;
    left: 48px; top: 110px;
    font-family: "Cormorant Garamond", serif;
    font-weight: 500;
    color: var(--ivory);
    font-size: 54px;
    line-height: 1.05;
  }
  .portrait {
    position: absolute;
    right: 0; top: 0;
    width: 340px; height: 400px;
    background: radial-gradient(ellipse at 55% 40%, var(--photo-light) 0%, var(--photo-mid) 35%, var(--photo-dark) 70%, var(--card-black) 100%);
  }
  .contact {
    position: absolute;
    left: 48px; bottom: 48px;
  }
  .person {
    font-family: "Cormorant Garamond", serif;
    font-weight: 500;
    font-size: 26px;
    color: var(--ivory);
  }
  .person .surname { color: var(--gold); }
  .phone {
    margin-top: 8px;
    display: flex; align-items: center; gap: 10px;
    font-family: "Montserrat", sans-serif;
    font-weight: 500;
    font-size: 17px;
    color: var(--ivory);
  }
  .phone-badge {
    width: 20px; height: 20px; border-radius: 50%;
    background: var(--gold);
    display: flex; align-items: center; justify-content: center;
  }
</style>
</head>
<body>

  <section class="card card-front" aria-label="Card front">
    <h1 class="business-name">Harbor Concierge</h1>
    <p class="email">quaylineerrands@mailvora.net</p>
  </section>

  <section class="card card-back" aria-label="Card back">
    <h2 class="title">Harbor<br>Concierge</h2>
    <div class="portrait" role="img" aria-label="Portrait photograph of Tamsin Heller"></div>
    <div class="contact">
      <p class="person">Tamsin <span class="surname">Heller</span></p>
      <p class="phone">
        <span class="phone-badge">
          <svg viewBox="0 0 24 24" width="12" height="12"><path d="M6.6 10.8a15 15 0 0 0 6.6 6.6l2.2-2.2a1 1 0 0 1 1-.25 11.4 11.4 0 0 0 3.6.57 1 1 0 0 1 1 1V20a1 1 0 0 1-1 1A17 17 0 0 1 3 4a1 1 0 0 1 1-1h3.5a1 1 0 0 1 1 1c0 1.25.2 2.45.57 3.57a1 1 0 0 1-.25 1Z" fill="#141414"/></svg>
        </span>
        305-482-9167
      </p>
    </div>
  </section>

</body>
</html>
```